Wollondilly ridge aerial works business card size advertising

I’m after a simple design , please see attached photo . Im after the same color green in the photo as the base color and the the little white man but instead of him holding a spanner i would like him to be holding a tv antenna pointing an angle , see attached photo of the antenna , i would like him on the left of the business card and the business name to fit in on the right with the phone number . ( if the antenna idea looks stupid , leave him holding a spanner ) On the reverse side of the card i would like a white background with green writing stating some of the services we provide which are the following .Antenna installations and repairs Wall mounting of tv’s Additional TV outlets Brolga satellite supply and installations Goulburn , Crookwell , Taralga , Tarago , Marulan , Collector , All rural areas All in all i would like the business card to compliment my invoices as pictured “ invoice supplied is a dummy invoice “

Contact Information for Business Card

wollondilly ridge aerial works 0418563927

Font styles to use
Sans Serif

Colors
9bcb3c

Requirements
Must have
• what i ask for in project description

```html
<!DOCTYPE html>
<html lang="en">
<head>
<meta charset="utf-8">
<title>Wollondilly Ridge Aerial Works – Business Card</title>
<link rel="stylesheet" href="https://fonts.googleapis.com/css2?family=Montserrat:wght@500;600;700&display=swap">
<style>
  :root {
    --base-green: #9bcb3c;
    --base-green-light: #b3d96a;
    --brand-green: #45b649;
    --text-grey: #3f3f3f;
    --card-white: #ffffff;
    --backdrop: #d9d9d9;
  }
  * { margin: 0; padding: 0; box-sizing: border-box; }
  html, body {
    width: 1200px;
    height: 1200px;
    overflow: hidden;
  }
  body {
    background: var(--backdrop);
    font-family: "Montserrat", sans-serif;
    position: relative;
  }
  .card {
    position: absolute;
    left: 240px;
    width: 720px;
    height: 420px;
    overflow: hidden;
  }
  .card--front {
    top: 142px;
    background: var(--base-green);
  }
  .card--back {
    top: 638px;
    background: var(--card-white);
  }

  .mascot-visual {
    position: absolute;
    left: 40px;
    top: 50px;
    width: 220px;
    height: 320px;
    border-radius: 6px;
    background: linear-gradient(160deg, var(--base-green-light) 0%, var(--base-green) 100%);
  }
  .business-name {
    position: absolute;
    left: 280px;
    width: 420px;
    top: 120px;
    text-align: center;
    color: var(--card-white);
    font-weight: 700;
    font-size: 34px;
    line-height: 44px;
    text-transform: uppercase;
  }
  .business-phone {
    position: absolute;
    left: 280px;
    width: 420px;
    top: 236px;
    text-align: center;
    color: var(--card-white);
    font-weight: 600;
    font-size: 42px;
    letter-spacing: 0.5px;
  }

  .services-intro {
    position: absolute;
    left: 56px;
    top: 40px;
    width: 600px;
    color: var(--brand-green);
    font-weight: 500;
    font-size: 19px;
    line-height: 28px;
  }
  .service-areas {
    position: absolute;
    left: 56px;
    top: 146px;
    list-style: none;
  }
  .service-areas li {
    position: relative;
    padding-left: 15px;
    color: var(--text-grey);
    font-weight: 500;
    font-size: 17px;
    line-height: 28px;
  }
  .service-areas li::before {
    content: "";
    position: absolute;
    left: 0;
    top: 11px;
    width: 6px;
    height: 6px;
    border-radius: 50%;
    background: var(--brand-green);
  }
  .invoice-note {
    position: absolute;
    left: 0;
    width: 100%;
    top: 366px;
    text-align: center;
    color: var(--brand-green);
    font-weight: 500;
    font-size: 19px;
  }
</style>
</head>
<body>
  <section class="card card--front">
    <div class="mascot-visual" role="img" aria-label="Little white figure holding a TV antenna pointing up at an angle"></div>
    <h1 class="business-name">Wollondilly Ridge<br>Aerial Works</h1>
    <p class="business-phone">0418563927</p>
  </section>

  <section class="card card--back">
    <p class="services-intro">Antenna installations and repairs Wall mounting of tv’s Additional TV outlets Brolga satellite supply and installations Goulburn</p>
    <ul class="service-areas">
      <li>Crookwell</li>
      <li>Taralga</li>
      <li>Tarago</li>
      <li>Marulan</li>
      <li>Collector</li>
      <li>All rural areas</li>
    </ul>
    <p class="invoice-note">invoice supplied is a dummy invoice</p>
  </section>
</body>
</html>
```